Design material for Lumora Summit

We need a design of POSM for Lumora Summit
1. Content:
- The Lumora Summit 3rd
- Singapore 28.10.2018
- A placeholder for insert logo of sponsors (limit 10 logo)
2. POSM:
- Backdrop: 5,5m and 2,6m
- Banner: 4m and 0,5m
- Standee: 0,8m and 2m
- Cover: A4 size
3. Style:
We need style simply because we are a hospital.
Main color: light blue and a little of green (if can)

Hope to see your design soon!

Font styles to use
Sans Serif

Colors
0792cd
85cae6
86cfc6
33b8a4
33a6d7

```html
<!DOCTYPE html>
<html lang="en">
<head>
<meta charset="utf-8">
<title>The Lumora Summit 3rd — Cover</title>
<link href="https://fonts.googleapis.com/css2?family=Montserrat:wght@800&family=Libre+Baskerville&display=swap" rel="stylesheet">
<style>
  :root {
    --teal-bg: #66cdc5;
    --photo-light: #eef8f7;
    --photo-mid: #b5e0db;
    --photo-deep: #86c4ba;
    --ink: #0d0d0d;
    --white: #ffffff;
  }
  html, body {
    margin: 0;
    padding: 0;
    overflow: hidden;
    background: var(--white);
  }
  .cover {
    position: relative;
    width: 849px;
    height: 1200px;
    background: var(--teal-bg);
    overflow: hidden;
  }
  .cover-art {
    position: absolute;
    inset: 0;
    width: 849px;
    height: 1200px;
  }
  .event-title {
    position: absolute;
    left: 57px;
    top: 803px;
    margin: 0;
    font-family: "Montserrat", sans-serif;
    font-weight: 800;
    font-size: 54px;
    line-height: 82px;
    letter-spacing: 0.24em;
    color: var(--ink);
    text-transform: uppercase;
    white-space: nowrap;
  }
  .location-bar {
    position: absolute;
    left: 57px;
    top: 996px;
    width: 600px;
    height: 57px;
    background: var(--ink);
    display: flex;
    align-items: center;
    padding-left: 22px;
    box-sizing: border-box;
  }
  .location {
    font-family: "Libre Baskerville", serif;
    font-size: 17px;
    letter-spacing: 0.12em;
    color: var(--white);
    text-transform: uppercase;
  }
</style>
</head>
<body>
  <main class="cover">
    <svg class="cover-art" viewBox="0 0 849 1200" xmlns="http://www.w3.org/2000/svg">
      <defs>
        <linearGradient id="labGlow" x1="0" y1="0" x2="0" y2="1">
          <stop offset="0" stop-color="var(--photo-light)"/>
          <stop offset="0.5" stop-color="var(--photo-mid)"/>
          <stop offset="1" stop-color="var(--photo-deep)"/>
        </linearGradient>
      </defs>
      <circle class="lab-photo" cx="608" cy="270" r="340" fill="url(#labGlow)"
              role="img" aria-label="Photo of laboratory flasks with plant cuttings on a wire rack, tinted teal"/>
      <g class="medical-cross" fill="none" stroke="var(--white)" stroke-width="13" stroke-linejoin="round">
        <circle cx="212" cy="467" r="145"/>
        <path d="M187 389 h50 a10 10 0 0 1 10 10 v43 h43 a10 10 0 0 1 10 10 v30 a10 10 0 0 1 -10 10 h-43 v43 a10 10 0 0 1 -10 10 h-50 a10 10 0 0 1 -10 -10 v-43 h-43 a10 10 0 0 1 -10 -10 v-30 a10 10 0 0 1 10 -10 h43 v-43 a10 10 0 0 1 10 -10 z"/>
      </g>
    </svg>
    <h1 class="event-title">The Lumora<br>Summit 3rd</h1>
    <div class="location-bar"><span class="location">Singapore</span></div>
  </main>
</body>
</html>
```